The merry loaf company. Wholesale gourmet pies to hospitality, needs a logo and flyer design

We need a flyer design for a new company based in Canberra ACT, called "the merry loaf company' Our flyer needs to describe our range of products, and delivery details. Our logo we would like to encompass a cartoon style chefs hat, love heart and pie. We like the idea of using red somewhere .

It Company

```html
<!DOCTYPE html>
<html lang="en">
<head>
<meta charset="utf-8">
<title>The Merry Loaf Company – Flyer</title>
<link rel="stylesheet" href="https://fonts.googleapis.com/css2?family=Special+Elite&family=Cormorant+Garamond:ital,wght@1,600;1,700&family=Open+Sans:wght@400;700&display=swap">
<style>
:root{
  --red:#d4070f;
  --red-dark:#a80008;
  --white:#ffffff;
  --ink:#111111;
  --page:#d9d9d9;
  --wood-light:#deb07a;
  --wood-mid:#c98f55;
  --wood-dark:#b87a42;
  --pill-grey:#cfcfcf;
}
*{margin:0;padding:0;box-sizing:border-box}
html,body{width:903px;height:1200px;overflow:hidden;background:var(--page)}
.flyer{position:absolute;left:58px;top:30px;width:800px;height:1115px;overflow:hidden;background:var(--white);box-shadow:0 4px 18px rgba(0,0,0,.25)}
.hero-photo{position:absolute;left:0;top:0;width:800px;height:340px;background:radial-gradient(ellipse at 72% 40%,#d9b88c 0%,#c49a6a 28%,#e8dfd6 55%,#f7f4f1 80%)}
.brand{position:absolute;left:30px;top:108px;display:flex;align-items:center;gap:10px;font-family:"Special Elite",monospace;font-size:21px;color:var(--ink)}
.brand-dot{width:52px;height:52px;border-radius:50%;background:var(--red)}
.wood{position:absolute;left:0;top:300px;width:800px;height:815px;background:linear-gradient(90deg,var(--wood-mid) 0%,var(--wood-light) 30%,var(--wood-mid) 50%,var(--wood-light) 51%,#e2b884 80%,var(--wood-mid) 100%)}
.band{position:absolute;left:0;top:0;width:800px;height:400px}
.headline{position:absolute;left:28px;top:262px;font-family:"Special Elite",monospace;font-size:62px;color:var(--white);letter-spacing:2px;transform:rotate(3.1deg);transform-origin:left top;white-space:nowrap}
.section-title{position:absolute;font-family:"Special Elite",monospace;font-size:31px;letter-spacing:1px}
.section-title.sweet{left:45px;top:358px;color:var(--red);text-shadow:0 0 2px #fff,0 0 2px #fff}
.section-title.savory{left:512px;top:420px;color:var(--ink)}
.intro{position:absolute;font-family:"Open Sans",sans-serif;font-size:13.4px;line-height:16.5px}
.intro.sweet{left:45px;top:403px;width:345px;color:var(--white)}
.intro.savory{left:420px;top:469px;width:330px;color:var(--red);text-align:right}
.pill{position:absolute;width:320px;height:78px;border-radius:39px;display:flex;align-items:center;font-family:"Cormorant Garamond",serif;font-style:italic;font-weight:700;font-size:38px;box-shadow:0 3px 6px rgba(0,0,0,.3)}
.pill.light{background:linear-gradient(90deg,var(--pill-grey),var(--white) 40%);color:var(--ink)}
.pill.bold{background:linear-gradient(90deg,var(--red-dark),var(--red) 50%);color:var(--white)}
.pill.sweet{left:38px;padding-left:100px}
.pill.savory{left:442px;padding-left:22px}
.pill .thumb{position:absolute;top:-6px;width:90px;height:90px;border-radius:50%;border:4px solid var(--red);background:radial-gradient(circle,#c58a4f,#8a5a30)}
.pill.sweet .thumb{left:-4px}
.pill.savory .thumb{right:-8px}
.pill .small{font-size:30px}
.footer{position:absolute;left:0;top:0;width:800px;height:1115px}
.order-label{position:absolute;left:447px;top:1008px;font-family:"Special Elite",monospace;font-size:29px;color:var(--white)}
.order-phone{position:absolute;left:398px;top:1050px;font-family:"Open Sans",sans-serif;font-weight:700;font-size:35px;color:var(--red)}
.web{position:absolute;left:35px;top:1076px;font-family:"Open Sans",sans-serif;font-size:20px;color:var(--white)}
</style>
</head>
<body>
<main class="flyer">
  <div class="hero-photo" role="img" aria-label="Close-up photo of a golden baked pie in a pastry case"></div>
  <div class="brand"><span class="brand-dot"></span>THE MERRY LOAF COMPANY</div>
  <div class="wood" role="img" aria-label="Light wooden board surface with a dusting of flour"></div>
  <svg class="band" viewBox="0 0 800 400" aria-hidden="true">
    <polygon points="0,222 800,262 800,385 0,322" fill="var(--red)"/>
  </svg>
  <h1 class="headline">CHOOSE YOUR WOW PIE</h1>

  <h2 class="section-title sweet">SWEET PIES</h2>
  <p class="intro sweet">The folks at The Merry Loaf Company use only the freshest ingredients, scouring our local farmer's market for the most delectable goodies to insert directly into our pies. All pies come in three sizes - 4, 6 and 9 inches except for key lime (4 and 9 inch only).</p>

  <div class="pill sweet light" style="top:531px"><span class="thumb" role="img" aria-label="Pumpkin pie slice with cream"></span>Pumpkin Pie</div>
  <div class="pill sweet bold" style="top:636px"><span class="thumb" role="img" aria-label="Golden apple pie"></span>Apple Pie</div>
  <div class="pill sweet light" style="top:741px"><span class="thumb" role="img" aria-label="Blueberry pie slices"></span>Blueberry Pie</div>
  <div class="pill sweet bold" style="top:843px"><span class="thumb" role="img" aria-label="Pecan pie"></span>Pecan Pie</div>
  <div class="pill sweet light" style="top:946px"><span class="thumb" role="img" aria-label="Key lime pie with cream"></span>Keylime Pie</div>

  <h2 class="section-title savory">SAVORY PIES</h2>
  <p class="intro savory">The folks at The Merry Loaf Company use only the freshest ingredients, scouring our local farmer's market for the most delectable goodies to insert directly into our pies.</p>

  <div class="pill savory light" style="top:566px"><span class="small">Chicken pot Pie</span><span class="thumb" role="img" aria-label="Chicken pot pies"></span></div>
  <div class="pill savory bold" style="top:671px"><span class="small">Butternut Squash</span><span class="thumb" role="img" aria-label="Butternut squash pie"></span></div>
  <div class="pill savory light" style="top:776px">Spinach Pie<span class="thumb" role="img" aria-label="Spinach pie slice"></span></div>
  <div class="pill savory bold" style="top:881px">Ruben Pie<span class="thumb" role="img" aria-label="Small individual pies"></span></div>

  <svg class="footer" viewBox="0 0 800 1115" aria-hidden="true">
    <path d="M0 1055 H370 C395 1055 395 990 430 990 H800 V1115 H0 Z" fill="var(--ink)"/>
  </svg>
  <p class="order-label">To order for pickup</p>
  <p class="order-phone">Call (555) 014-2290</p>
  <p class="web">www.themerryloafcompany.net</p>
</main>
</body>
</html>
```